Korvell Plant Services

We are a heavy diesel mechanical business with additional air con certificates, remapping engine rebuilt

Contact Information for Business Card

Company Name, Director Name, Managing Director, Contact details, email and website

Font styles to use
Serif
Script

```html
<!DOCTYPE html>
<html lang="en">
<head>
<meta charset="UTF-8">
<title>Korvell Plant Services – Business Card</title>
<link href="https://fonts.googleapis.com/css2?family=Poppins:wght@400;500;700;800&display=swap" rel="stylesheet">
<style>
  :root {
    --brand-indigo: #2d287a;
    --ink: #111114;
    --paper: #ffffff;
    --stage: #e7e7ec;
    --rule: #9a98b8;
  }
  * { box-sizing: border-box; margin: 0; padding: 0; }
  html, body { width: 1200px; height: 800px; overflow: hidden; }
  body {
    background: var(--stage);
    font-family: "Poppins", sans-serif;
    color: var(--ink);
    position: relative;
  }
  .card {
    position: absolute;
    top: 250px;
    width: 525px;
    height: 300px;
    border-radius: 20px;
    overflow: hidden;
    box-shadow: 0 10px 28px rgba(0,0,0,0.18);
  }
  /* Back */
  .card-back { left: 50px; background: var(--brand-indigo); color: var(--paper); }
  .card-back .brand {
    position: absolute; left: 0; right: 0; top: 104px;
    display: flex; align-items: center; justify-content: center; gap: 12px;
  }
  .brand-dot { width: 22px; height: 22px; border-radius: 50%; background: currentColor; flex: none; }
  .brand-name { font-weight: 800; font-size: 26px; line-height: 1.1; letter-spacing: 0.2px; }
  .card-back .web {
    position: absolute; bottom: 30px; left: 0; right: 0; text-align: center;
    font-size: 13px; font-weight: 500; letter-spacing: 0.3px;
  }
  /* Front */
  .card-front { left: 625px; background: var(--brand-indigo); }
  .card-front .face { position: absolute; inset: 0; }
  .card-front .brand {
    position: absolute; left: 30px; top: 128px; width: 200px;
    display: flex; align-items: center; gap: 10px; color: var(--brand-indigo);
  }
  .card-front .brand-name { font-size: 21px; }
  .divider {
    position: absolute; left: 250px; top: 62px; width: 1px; height: 176px;
    background: var(--rule);
  }
  .contact { position: absolute; left: 272px; top: 70px; width: 180px; }
  .person-name { font-weight: 700; font-size: 21px; line-height: 1.1; }
  .person-role { font-size: 13.5px; margin-top: 3px; margin-bottom: 18px; }
  .contact-line {
    display: flex; align-items: center; gap: 7px;
    font-size: 10.5px; margin-bottom: 8px; white-space: nowrap;
  }
  .contact-line svg { width: 11px; height: 11px; flex: none; }
</style>
</head>
<body>
  <section class="card card-back">
    <div class="brand">
      <span class="brand-dot"></span>
      <span class="brand-name">Korvell Plant Services</span>
    </div>
    <p class="web">www.korvellplant.com</p>
  </section>

  <section class="card card-front">
    <svg class="face" viewBox="0 0 525 300" width="525" height="300" aria-hidden="true">
      <path d="M0 0 H430 C500 20 505 280 440 300 H0 Z" fill="#111114"/>
      <path d="M0 0 H420 C488 22 492 278 428 300 H0 Z" fill="#ffffff"/>
    </svg>
    <div class="brand">
      <span class="brand-dot"></span>
      <span class="brand-name">Korvell Plant Services</span>
    </div>
    <div class="divider"></div>
    <div class="contact">
      <p class="person-name">Daniel Harrow</p>
      <p class="person-role">Managing Director</p>
      <p class="contact-line">
        <svg viewBox="0 0 24 24"><path fill="#2d287a" d="M6.6 10.8a15 15 0 0 0 6.6 6.6l2.2-2.2c.3-.3.7-.4 1-.2 1.1.4 2.3.6 3.6.6.6 0 1 .4 1 1V20c0 .6-.4 1-1 1A17 17 0 0 1 3 4c0-.6.4-1 1-1h3.5c.6 0 1 .4 1 1 0 1.3.2 2.5.6 3.6.1.3 0 .7-.2 1z"/></svg>
        1300-555-018
      </p>
      <p class="contact-line">
        <svg viewBox="0 0 24 24"><rect x="2" y="5" width="20" height="14" rx="1" fill="#2d287a"/><path d="M2 6l10 7 10-7" stroke="#fff" stroke-width="1.6" fill="none"/></svg>
        info@korvellplant.com
      </p>
      <p class="contact-line">
        <svg viewBox="0 0 24 24"><circle cx="12" cy="12" r="10" fill="#2d287a"/><path d="M2 12h20M12 2c3 3 3 17 0 20M12 2c-3 3-3 17 0 20" stroke="#fff" stroke-width="1.4" fill="none"/></svg>
        www.korvellplant.com
      </p>
    </div>
  </section>
</body>
</html>
```